Billboard design for a small town Oral Surgeon

We are getting several billboards and need a design that highlights the doctors photo, and bullet points of what he does. Our business name is extremely long, so it’s a challenge to figure out how to do this. Maybe just use our logo? Open to ideas.
The logo can be shortened as designer sees fit, meaning we can drop the tag line. Important info to include:
Doctors name is Lorvik Tamsen
The highlighted bullet points are:
•Implants
•wisdom teeth
•Jaw Surgery
•facial trauma
The goal of this billboard is to let our community know that they have an option here in Ada, our town. Many still drive to the city a couple hours away not knowing they now have an option here at home. Having a hard time finding examples of what I have in mind, so hoping this will get us going. I want it as “non-busy” as possible, so no unnecessary lines or anything that competes with the information we are trying to get across.

Target Market(s)

Everyone in town, just trying to spread the word that we are here

Industry/Entity Type

Medical/surgical (oral surgery)

Font styles to use
Sans Serif

Colors
0094D4
00A9DD
6FCCEA
C7EBF8
E9F6FB

Requirements
Must have
• *New note** Due to location of billboard, I prefer the photo of doctor to be on the left side. Must look neat and professional. Must highlight what we do.
Nice to have
• Our colors are a blue-green with silver, against black or white, but I’m flexible on this, I don’t necessarily need the colors highlighted. I’m also flexible on font style, just needs to be easy to read.
Should not have
• Distracting graphics, should not look like a dental office. That’s an issue we have is people thinking we are another dental office, we do not do any general dentistry, it’s surgery only.

```html
<!DOCTYPE html>
<html lang="en">
<head>
<meta charset="utf-8">
<title>Red River Valley Oral &amp; Facial Surgery – Billboard</title>
<link rel="stylesheet" href="https://fonts.googleapis.com/css2?family=Oswald:wght@400&family=Montserrat:wght@400;600&display=swap">
<style>
  :root {
    --page-bg: #474747;
    --board-white: #ffffff;
    --brand-teal: #0d889f;
    --brand-silver: #9a9a9c;
    --ink-dark: #2b2b2b;
    --portrait-top: #e9e6e3;
    --portrait-mid: #cf9b84;
    --portrait-low: #1f2a3c;
  }
  * { box-sizing: border-box; margin: 0; padding: 0; }
  html, body {
    width: 921px;
    height: 1200px;
    overflow: hidden;
    background: var(--page-bg);
  }
  .canvas {
    position: relative;
    width: 921px;
    height: 1200px;
  }
  .billboard {
    position: absolute;
    left: 28px;
    top: 474px;
    width: 865px;
    height: 252px;
    background: var(--board-white);
  }
  .billboard svg { display: block; width: 100%; height: 100%; }
  .service-list text {
    font-family: "Oswald", "Arial Narrow", sans-serif;
    font-size: 56px;
    fill: var(--board-white);
  }
  .practice-name {
    font-family: "Montserrat", Arial, sans-serif;
    font-weight: 600;
    font-size: 36px;
    fill: var(--ink-dark);
  }
  .practice-line {
    font-family: "Montserrat", Arial, sans-serif;
    font-weight: 400;
    font-size: 24px;
    fill: var(--brand-teal);
  }
  .phone-number {
    font-family: "Montserrat", Arial, sans-serif;
    font-weight: 600;
    font-size: 33px;
    fill: var(--board-white);
  }
</style>
</head>
<body>
<main class="canvas">
  <section class="billboard" aria-label="Red River Valley Oral and Facial Surgery billboard">
    <svg viewBox="0 0 1578 460" xmlns="http://www.w3.org/2000/svg">
      <defs>
        <linearGradient id="portraitTone" x1="0" y1="0" x2="0" y2="1">
          <stop offset="0" stop-color="var(--portrait-top)"/>
          <stop offset="0.45" stop-color="var(--portrait-mid)"/>
          <stop offset="1" stop-color="var(--portrait-low)"/>
        </linearGradient>
      </defs>

      <!-- silver accent band behind the panel edge -->
      <path class="accent-band" d="M262,0 H320 L230,200 L205,200 Z" fill="var(--brand-silver)"/>

      <!-- teal service panel -->
      <path class="service-panel" d="M296,0 L815,0 C868,70 895,150 895,230 C895,310 868,390 815,460 L200,460 Z" fill="var(--brand-teal)"/>

      <!-- doctor portrait area -->
      <path class="doctor-portrait" role="img" aria-label="Portrait photo of Dr. Lorvik Tamsen, smiling, in a dark suit, white shirt and red tie"
            d="M0,40 H300 L300,300 L435,460 H0 Z" fill="url(#portraitTone)"/>

      <!-- services -->
      <g class="service-list">
        <g class="service-item">
          <circle cx="436" cy="122" r="22" fill="var(--board-white)"/>
          <path d="M426,122 l7,7 l13,-14" fill="none" stroke="var(--brand-teal)" stroke-width="4" stroke-linecap="round" stroke-linejoin="round"/>
          <text x="474" y="143">Implants</text>
        </g>
        <g class="service-item">
          <circle cx="436" cy="192" r="22" fill="var(--board-white)"/>
          <path d="M426,192 l7,7 l13,-14" fill="none" stroke="var(--brand-teal)" stroke-width="4" stroke-linecap="round" stroke-linejoin="round"/>
          <text x="474" y="213">Wisdom teeth</text>
        </g>
        <g class="service-item">
          <circle cx="436" cy="262" r="22" fill="var(--board-white)"/>
          <path d="M426,262 l7,7 l13,-14" fill="none" stroke="var(--brand-teal)" stroke-width="4" stroke-linecap="round" stroke-linejoin="round"/>
          <text x="474" y="283">Jaw Surgery</text>
        </g>
        <g class="service-item">
          <circle cx="436" cy="332" r="22" fill="var(--board-white)"/>
          <path d="M426,332 l7,7 l13,-14" fill="none" stroke="var(--brand-teal)" stroke-width="4" stroke-linecap="round" stroke-linejoin="round"/>
          <text x="474" y="353">Facial trauma</text>
        </g>
      </g>

      <!-- practice name -->
      <g class="practice-lockup" text-anchor="middle">
        <text class="practice-name" x="1240" y="170">RED RIVER VALLEY</text>
        <text class="practice-name" x="1240" y="218">ORAL &amp; FACIAL SURGERY</text>
        <text class="practice-line" x="1240" y="268">Now serving Ada, right here at home</text>
      </g>

      <!-- phone pill -->
      <g class="phone-pill">
        <rect x="1074" y="330" width="332" height="56" rx="28" fill="var(--brand-teal)"/>
        <g class="globe-icon" fill="none" stroke-width="2.5">
          <circle cx="1105" cy="358" r="20" fill="var(--board-white)"/>
          <circle cx="1105" cy="358" r="14" stroke="var(--brand-teal)"/>
          <ellipse cx="1105" cy="358" rx="6" ry="14" stroke="var(--brand-teal)"/>
          <line x1="1091" y1="358" x2="1119" y2="358" stroke="var(--brand-teal)"/>
        </g>
        <text class="phone-number" x="1137" y="370">(580) 555-0148</text>
      </g>
    </svg>
  </section>
</main>
</body>
</html>
```